Site for a workout and Consulting enterprise

I need a professional responsive site for www.valomer.hamburg. The website shoulderstand consist of a Landing and 4 other pages. - On page for the contact informations - on page for the about - on page for consulting services (technical) - on page for Training and workshop services (business and soft skills) I add some files so you can see my idea of the design.
Target Market(s)
IT and Management
Industry/Entity Type
Management Consulting
Coding
Coded - Design and coding required
Number of Pages Required
4 page
Requirements
Must have
- Use Pictures for Background, Sliders and Topics. Just have to placeholders for the design.

```html
<!DOCTYPE html>
<html lang="de">
<head>
<meta charset="utf-8">
<title>Valomer – Individuen, Ideen, Innovationen</title>
<link href="https://fonts.googleapis.com/css2?family=Open+Sans:wght@400;600&family=Roboto:wght@400&display=swap" rel="stylesheet">
<style>
  :root{
    --white:#ffffff;
    --blue:#3a8fd6;
    --wood-dark:#2e251d;
    --wood-mid:#6b5641;
    --wood-light:#a68c6c;
    --paper:#d9c6a3;
    --shade-left:rgba(10,10,10,.66);
    --shade-right:rgba(10,10,10,.2);
    --rule:rgba(255,255,255,.75);
  }
  *{box-sizing:border-box;margin:0;padding:0}
  html,body{width:1200px;height:646px;overflow:hidden;background:var(--wood-dark)}
  body{font-family:"Open Sans",sans-serif;color:var(--white);position:relative}
  .hero-photo{position:absolute;inset:0;
    background:
      radial-gradient(ellipse 150px 190px at 960px 440px,rgba(217,198,163,.75) 0%,rgba(217,198,163,0) 100%),
      radial-gradient(ellipse 120px 90px at 880px 150px,rgba(200,170,130,.6) 0%,rgba(200,170,130,0) 100%),
      radial-gradient(ellipse 130px 110px at 230px 480px,rgba(170,130,90,.55) 0%,rgba(170,130,90,0) 100%),
      radial-gradient(ellipse 120px 90px at 260px 110px,rgba(170,135,95,.5) 0%,rgba(170,135,95,0) 100%),
      radial-gradient(ellipse 110px 80px at 700px 560px,rgba(210,190,160,.45) 0%,rgba(210,190,160,0) 100%),
      repeating-linear-gradient(180deg,rgba(0,0,0,0) 0px,rgba(0,0,0,0) 46px,rgba(0,0,0,.12) 50px,rgba(0,0,0,0) 54px),
      radial-gradient(ellipse at 70% 45%,var(--wood-light) 0%,var(--wood-mid) 50%,var(--wood-dark) 100%);}
  .shade-left{position:absolute;left:0;top:0;width:595px;height:646px;background:var(--shade-left)}
  .shade-right{position:absolute;left:595px;top:0;right:0;height:646px;background:var(--shade-right)}
  .brand{position:absolute;left:291px;top:240px;width:270px}
  .brand-name{font-size:70px;font-weight:400;line-height:1;letter-spacing:1px;display:block}
  .brand-tagline{font-family:"Roboto",sans-serif;font-size:19.5px;margin-top:22px;display:block;white-space:nowrap}
  .topics{position:absolute;left:0;top:0;width:1200px;height:646px}
  .topic-label{position:absolute;font-size:14px;line-height:20.5px}
  .menu-button{position:absolute;left:1073px;top:26px;width:39px;height:39px;border:1.5px solid var(--white);border-radius:50%}
  .menu-button span{position:absolute;left:10px;width:17px;height:2.5px;background:var(--white);border-radius:1px}
  .footer-rule{position:absolute;left:89px;top:573px;width:1023px;height:1px;background:var(--rule)}
  .copyright{position:absolute;left:92px;top:601px;font-size:14.5px}
  .social{position:absolute;left:529px;top:598px;display:flex;gap:7px}
  .social-link{width:27px;height:27px;border:1.5px solid var(--white);border-radius:50%;display:flex;align-items:center;justify-content:center}
  .social-link i{display:block;width:9px;height:9px;background:var(--white);border-radius:1.5px}
  .legal{position:absolute;right:90px;top:598px;font-size:14.5px}
  .legal span{margin:0 8px}
</style>
</head>
<body>
  <div class="hero-photo" role="img" aria-label="Hintergrundfoto: Hände arrangieren Holzklötze, Puzzleteile und einen Notizblock mit Glühbirnenskizze auf einem Holztisch"></div>
  <div class="shade-left"></div>
  <div class="shade-right"></div>

  <div class="brand">
    <span class="brand-name">Valomer</span>
    <span class="brand-tagline">Individuen, Ideen, Innovationen</span>
  </div>

  <svg class="topics" viewBox="0 0 1200 646" aria-hidden="true">
    <path d="M595 256 A66 66 0 0 1 595 388 Z" fill="var(--blue)"/>
    <rect x="600" y="319" width="34" height="7" fill="var(--white)"/>
    <rect x="613.5" y="305" width="7" height="35" fill="var(--white)"/>
    <g stroke="var(--blue)" stroke-width="1.2" fill="none">
      <line x1="628" y1="268" x2="648" y2="252"/>
      <line x1="661" y1="320" x2="670" y2="320"/>
      <line x1="628" y1="375" x2="648" y2="388"/>
      <circle cx="662" cy="239" r="20"/>
      <circle cx="690" cy="314" r="20"/>
      <circle cx="663" cy="400" r="20"/>
    </g>
    <g fill="var(--white)">
      <circle cx="662" cy="239" r="6"/>
      <circle cx="662" cy="239" r="8" fill="none" stroke="var(--white)" stroke-width="3" stroke-dasharray="3 2.3"/>
      <circle cx="662" cy="239" r="2.3" fill="var(--wood-dark)"/>
      <rect x="682" y="307" width="16" height="11" rx="1" fill="none" stroke="var(--white)" stroke-width="1.6"/>
      <rect x="679" y="319" width="22" height="2"/>
      <path d="M657 391 h8 l5 5 v13 h-13 z"/>
    </g>
    <line x1="1152" y1="288" x2="1169" y2="306" stroke="var(--white)" stroke-width="1"/>
    <circle cx="1152" cy="288" r="4.5" fill="var(--blue)"/>
    <g fill="var(--white)">
      <circle cx="1169" cy="306" r="4.5"/>
      <circle cx="1169" cy="323" r="4.5"/>
      <circle cx="1169" cy="341" r="4.5"/>
      <circle cx="1169" cy="358" r="4.5"/>
    </g>
  </svg>

  <div class="topic-label" style="left:689px;top:206px">porro ipsum<br>Neque porro<br>&nbsp;Quisquam</div>
  <div class="topic-label" style="left:717px;top:286px">Dolorem<br>Ipsum quia<br>Consectetur</div>
  <div class="topic-label" style="left:690px;top:372px">porro ipsum<br>&nbsp;Neque porro<br>&nbsp;Quisquam</div>

  <div class="menu-button" aria-label="Menü"><span style="top:13px"></span><span style="top:18px"></span><span style="top:23px"></span></div>

  <div class="footer-rule"></div>
  <div class="copyright">Copyright © 2017. All Rights Reserved</div>
  <div class="social" aria-label="Soziale Netzwerke">
    <span class="social-link"><i></i></span>
    <span class="social-link"><i></i></span>
    <span class="social-link"><i></i></span>
    <span class="social-link"><i></i></span>
  </div>
  <div class="legal">Impressum<span>|</span>Kontakt</div>
</body>
</html>
```